Customs House descriptive business cards

We require a two-sided business card that has a simple yet elegant design. We want to be able to promote our services as a customs house. This card should include our logo, contact info and services offered with the logo being on one side and the contact info and services on the flip side

Target Market(s)

Importers / exporters to and from the Bahamas

Industry/Entity Type

Logistics

Contact Information for Business Card

The front side of the card could have the logo and the flip side should have the other relevant info

Font styles to use
Serif

Colors

Designer to choose colors to be used in the design.

Requirements
Must have
• (Harbourline Agents Ltd) Logo, address and contact info also services:
• import customs clearance, Delivery & HAndling services,Florida pickups, Export packing & Crating Services, export customs clearance, Consulting

```html
<!DOCTYPE html>
<html lang="en">
<head>
<meta charset="utf-8">
<title>Harbourline Agents Ltd – Business Card</title>
<link href="https://fonts.googleapis.com/css2?family=Tinos:wght@400;700&display=swap" rel="stylesheet">
<style>
  :root {
    --brand-blue: #2888cb;
    --text-grey: #7a7a7a;
    --paper: #ffffff;
    --backdrop: #ededed;
  }
  * { box-sizing: border-box; margin: 0; padding: 0; }
  html, body { width: 1200px; height: 1200px; overflow: hidden; }
  body {
    background: var(--backdrop);
    font-family: "Tinos", "Times New Roman", serif;
    position: relative;
  }
  .card {
    position: absolute;
    left: 235px;
    width: 701px;
    height: 378px;
  }
  .card--front { top: 165px; background: var(--paper); }
  .card--back { top: 635px; background: var(--brand-blue); }

  .brand {
    position: absolute;
    top: 30px;
    left: 0;
    width: 100%;
    height: 96px;
    display: flex;
    justify-content: center;
    align-items: center;
    gap: 14px;
  }
  .brand__dot {
    width: 40px; height: 40px;
    border-radius: 50%;
    background: var(--brand-blue);
  }
  .brand__divider {
    width: 2px; height: 96px;
    background: var(--brand-blue);
  }
  .brand__name {
    color: var(--brand-blue);
    font-size: 32px;
    letter-spacing: 2px;
    font-weight: 400;
  }

  .person { position: absolute; left: 30px; top: 163px; }
  .person__name {
    font-size: 25px;
    line-height: 1;
    color: var(--brand-blue);
    letter-spacing: 0.2px;
  }
  .person__name .surname { color: var(--text-grey); }
  .person__title {
    margin-top: 5px;
    display: flex;
    align-items: center;
    gap: 4px;
    color: var(--brand-blue);
    font-size: 13px;
    letter-spacing: 0.4px;
  }
  .person__title::before, .person__title::after {
    content: ""; width: 26px; height: 3px; background: var(--brand-blue);
  }

  .social {
    position: absolute;
    right: 31px; top: 173px;
    display: flex; align-items: center; gap: 4px;
    color: var(--text-grey);
    font-weight: 700; font-size: 13.5px;
  }
  .social__dot { width: 32px; height: 32px; border-radius: 50%; background: var(--brand-blue); }
  .social__label { margin-left: 6px; }

  .rule {
    position: absolute;
    left: 30px; top: 210px;
    width: 640px; height: 3px;
    background: var(--brand-blue);
  }

  .services {
    position: absolute;
    left: 30px; top: 226px;
    width: 640px;
    color: var(--brand-blue);
    font-size: 10.5px;
    font-weight: 700;
    line-height: 16px;
    letter-spacing: 0.3px;
    text-transform: uppercase;
  }
  .services span + span::before { content: " • "; color: var(--text-grey); }

  .contacts { position: absolute; left: 30px; top: 275px; list-style: none; }
  .contacts li {
    display: flex; align-items: center;
    height: 26px;
    color: var(--text-grey);
    font-weight: 700;
    font-size: 11.5px;
    text-transform: uppercase;
  }
  .contacts li.phone { font-size: 13.5px; text-transform: none; }
  .contacts svg { width: 22px; height: 20px; margin-right: 10px; fill: var(--brand-blue); }

  .address {
    position: absolute;
    left: 432px; top: 316px;
    color: var(--text-grey);
    font-weight: 700;
    font-size: 11px;
    line-height: 18px;
    font-style: normal;
    text-transform: uppercase;
  }

  .back-name {
    position: absolute; inset: 0;
    display: flex; align-items: center; justify-content: center;
    color: var(--paper);
    font-size: 40px;
    letter-spacing: 3px;
    font-weight: 400;
  }
</style>
</head>
<body>
  <section class="card card--front" aria-label="Business card front">
    <div class="brand">
      <span class="brand__dot"></span>
      <span class="brand__divider"></span>
      <span class="brand__name">HARBOURLINE AGENTS LTD</span>
    </div>

    <div class="person">
      <p class="person__name">MARCUS <span class="surname">DELANEY</span></p>
      <p class="person__title">OPERATIONS DIRECTOR</p>
    </div>

    <div class="social">
      <span class="social__dot"></span>
      <span class="social__dot"></span>
      <span class="social__label">Harbourline Agents Ltd.</span>
    </div>

    <div class="rule"></div>

    <p class="services">
      <span>Import customs clearance</span><span>Delivery &amp; handling services</span><span>Florida pickups</span><br>
      <span>Export packing &amp; crating services</span><span>Export customs clearance</span><span>Consulting</span>
    </p>

    <ul class="contacts">
      <li class="phone">
        <svg viewBox="0 0 24 20" aria-hidden="true"><path d="M2 7c0-3 5-5 10-5s10 2 10 5v2h-5V7c-1-1-3-1.5-5-1.5S8 6 7 7v2H2z"/><path d="M6 10h12l2 8H4z"/><circle cx="12" cy="14" r="2.3" fill="#fff"/></svg>
        (242)555-0184 - (242) 555-0127
      </li>
      <li>
        <svg viewBox="0 0 24 20" aria-hidden="true"><rect x="2" y="3" width="20" height="14"/><path d="M3 4l9 7 9-7" fill="none" stroke="#fff" stroke-width="1.6"/><path d="M3 16l7-6M21 16l-7-6" stroke="#fff" stroke-width="1.2"/></svg>
        imports@harbourlineagents.com
      </li>
      <li>
        <svg viewBox="0 0 24 24" aria-hidden="true"><circle cx="12" cy="12" r="11"/><path d="M6 6c2 1 3 3 2 5s1 3 2 5-1 4-1 5M14 3c1 2 3 2 4 4s-1 3 0 5 3 2 3 3" fill="none" stroke="#fff" stroke-width="1.6"/></svg>
        www.harbourlineagents.com
      </li>
    </ul>

    <address class="address">
      42 Coral Ridge Road, P.O. Box SP-70214<br>
      Nassau, Bahamas
    </address>
  </section>

  <section class="card card--back" aria-label="Business card back">
    <p class="back-name">HARBOURLINE AGENTS LTD</p>
  </section>
</body>
</html>
```